Business Card & Stationary Design Project

We are looking for some creative direction for business cards and our stationary.

We are a global logistics firm that has recently changed its name to Marwick Global Logistics and we have a new website due out tomorrow (www.marwick.com.au).

The colours of the company are rich navy tones, I would like to have business cards that fit together to make one picture on the back (possibly an old map of the world??), and the front to be modern contemporary looking.

But I am open to suggestions, so just incorporate our new logo and get going!
Updates

Hi Everyone,

Thank you for all of your designs so far and the time you have put into it.

I have asked many of you for amendments to see if we can get a final product, so with this in mind I am extending the deadline by a few days.

Good luck and thank you once again.

Please message me direct if you need any clarification.

Kind Regards
Tobias

Reason: As outlined the extra 3 days is for amendments and changes to the current submissions. Thanks Tobias

Industry/Entity Type

Business

```html
<!DOCTYPE html>
<html lang="en">
<head>
<meta charset="utf-8">
<title>Marwick Global Logistics – Business Card Back</title>
<link rel="stylesheet" href="https://fonts.googleapis.com/css2?family=Cinzel:wght@400&display=swap">
<style>
  :root {
    --page: #ffffff;
    --card-edge: #c9c4ba;
    --parchment-light: #f1ebdf;
    --parchment-mid: #e6dccb;
    --parchment-dark: #d6c8b0;
    --navy: #16164a;
    --globe-light: #8fd0ff;
    --globe-mid: #1f7fd6;
    --globe-deep: #0a3f8f;
  }
  html, body {
    margin: 0;
    padding: 0;
    width: 1200px;
    height: 686px;
    overflow: hidden;
    background: var(--page);
  }
  .card {
    position: relative;
    width: 1196px;
    height: 682px;
    margin: 2px;
    border-radius: 30px;
    overflow: hidden;
    box-shadow: 0 0 0 1px var(--card-edge);
  }
  .card__map {
    position: absolute;
    inset: 0;
    background:
      radial-gradient(ellipse at 45% 45%, var(--parchment-light) 0%, var(--parchment-mid) 60%, var(--parchment-dark) 100%);
  }
  .brand {
    position: absolute;
    left: 86px;
    top: 262px;
    color: var(--navy);
    font-family: "Cinzel", "Times New Roman", serif;
    font-weight: 400;
  }
  .brand__name {
    margin: 0;
    font-size: 78px;
    line-height: 1;
    letter-spacing: 0.4em;
    font-weight: 400;
  }
  .brand__tagline {
    margin: 10px 0 0 2px;
    font-size: 30px;
    line-height: 1;
    letter-spacing: 0.78em;
    font-variant: small-caps;
    text-transform: capitalize;
  }
  .card__globe {
    position: absolute;
    left: 772px;
    top: 161px;
    width: 290px;
    height: 290px;
    border-radius: 50%;
    background: radial-gradient(circle at 38% 28%, var(--globe-light) 0%, var(--globe-mid) 45%, var(--globe-deep) 100%);
  }
</style>
</head>
<body>
  <div class="card">
    <div class="card__map" role="img" aria-label="Antique engraved map of the world in sepia tones"></div>
    <div class="brand">
      <h1 class="brand__name">MARWICK</h1>
      <p class="brand__tagline">Global Logistics</p>
    </div>
    <div class="card__globe" role="img" aria-label="Glossy blue globe showing Asia and Australia"></div>
  </div>
</body>
</html>
```